Brisk Morsels
Business Card and Stationary Design
Brisk Morsels -
Creative Brief
Bright & Fun-filled
Gordon T Welham
Owner
41 Harlow Lane Millbrook Ridge, NJ 08637
Gord.Welham@postmailer.example
www.brisk-morsels.example
Looking for something simple, but eye-catching. Looking for a variety of different fonts/styles/backgrounds to achieve: -Seamless integration with the attached logo. -Backgrounds to enhance the "pop" of the logo. -Professional, but with a hint of fun. The Brisk Morsel will compete in the energy drink/shot industry (e.g. Tan Lynx and Nine Minute Vigor). We differentiate ourselves through superior taste and natural ingredients, creating a more satisfying experience for the energy consumer. Feel free to message me with any questions/concerns/comments.

```html
<!DOCTYPE html>
<html lang="en">
<head>
<meta charset="utf-8">
<title>Brisk Morsels – Business Card</title>
<link rel="stylesheet" href="https://fonts.googleapis.com/css2?family=Open+Sans:wght@400;600;700;800&display=swap">
<style>
  :root{
    --stage:#1c1c1c;
    --card-white:#ffffff;
    --brown:#8a6238;
    --brown-dark:#5a3c1e;
    --brown-light:#b98e5c;
    --orange:#e0782b;
    --ink:#3a3a3a;
    --muted:#6b6b6b;
  }
  *{margin:0;padding:0;box-sizing:border-box;}
  html,body{width:1200px;height:571px;overflow:hidden;}
  body{background:var(--stage);font-family:"Open Sans",Arial,sans-serif;position:relative;}
  .card{position:absolute;top:149px;width:512px;height:331px;border-radius:24px;overflow:hidden;box-shadow:0 6px 18px rgba(0,0,0,.55);}
  .card--front{left:53px;background:var(--card-white);}
  .card--back{left:612px;background:radial-gradient(ellipse at 50% 45%,var(--brown-light) 0%,var(--brown) 55%,var(--brown-dark) 100%);}
  .card__pattern{position:absolute;inset:0;background:linear-gradient(180deg,#f6f3ef 0%,#ffffff 60%);}
  .card__wave{position:absolute;inset:0;width:100%;height:100%;}
  .wordmark{position:absolute;display:flex;align-items:center;gap:10px;font-weight:800;color:var(--orange);letter-spacing:-.5px;}
  .wordmark__dot{width:18px;height:18px;border-radius:50%;background:var(--orange);flex:none;}
  .card--front .wordmark{left:30px;top:128px;font-size:34px;}
  .card--back .wordmark{left:50%;top:128px;transform:translateX(-50%);font-size:44px;color:#fff;white-space:nowrap;}
  .card--back .wordmark__dot{background:#fff;}
  .person{position:absolute;left:282px;top:56px;}
  .person__name{font-size:15px;font-weight:600;color:var(--ink);}
  .person__role{font-size:10px;color:var(--muted);margin-top:2px;}
  .contact{position:absolute;left:282px;top:172px;font-size:10px;color:var(--ink);line-height:1.45;}
  .contact__address{margin-bottom:8px;}
  .contact__row{display:flex;align-items:center;gap:7px;}
  .contact__row svg{width:11px;height:11px;flex:none;fill:var(--brown);}
  .site{position:absolute;left:0;right:0;bottom:30px;text-align:center;color:#fff;font-weight:700;font-size:15px;letter-spacing:2px;}
</style>
</head>
<body>
  <section class="card card--front" aria-label="Business card front">
    <div class="card__pattern" role="img" aria-label="Faint circular pattern background"></div>
    <svg class="card__wave" viewBox="0 0 512 331" preserveAspectRatio="none" aria-hidden="true">
      <path d="M0 215 C120 205 220 250 300 290 C350 315 420 325 512 318 L512 331 L0 331 Z" fill="#8a6238"/>
      <path d="M0 205 C120 195 220 238 300 278 C350 303 420 313 512 308 L512 312 C420 318 350 308 300 284 C220 245 120 202 0 212 Z" fill="#e0782b"/>
    </svg>
    <div class="wordmark"><span class="wordmark__dot"></span>Brisk Morsels</div>
    <div class="person">
      <div class="person__name">Gordon T Welham</div>
      <div class="person__role">Owner</div>
    </div>
    <div class="contact">
      <div class="contact__address">41 Harlow Lane<br>Millbrook Ridge, NJ 08637</div>
      <div class="contact__row"><svg viewBox="0 0 24 24"><path d="M6.6 10.8a15 15 0 006.6 6.6l2.2-2.2a1 1 0 011-.25 11.4 11.4 0 003.6.57 1 1 0 011 1V20a1 1 0 01-1 1A17 17 0 013 4a1 1 0 011-1h3.5a1 1 0 011 1c0 1.25.2 2.45.57 3.57a1 1 0 01-.25 1z"/></svg>(555) 014-2290</div>
      <div class="contact__row"><svg viewBox="0 0 24 24"><path d="M2 5h20v14H2z M2 5l10 8 10-8" stroke="#fff" stroke-width="1.5"/></svg>Gord.Welham@postmailer.example</div>
      <div class="contact__row"><svg viewBox="0 0 24 24"><path d="M12 2a7 7 0 00-7 7c0 5 7 13 7 13s7-8 7-13a7 7 0 00-7-7zm0 9.5A2.5 2.5 0 1112 6.5a2.5 2.5 0 010 5z"/></svg>www.brisk-morsels.example</div>
    </div>
  </section>

  <section class="card card--back" aria-label="Business card back">
    <div class="wordmark"><span class="wordmark__dot"></span>Brisk Morsels</div>
    <div class="site">www.brisk-morsels.example</div>
  </section>
</body>
</html>
```